Business Card Design Project

We are a commercial talent casting company, a very "now" company. We need a new business card that is both current, graphic and elegantly interesting. As we are a service business,
we need something that will attract the attention of new clients,
yet project a business that is 25 years old.

Industry/Entity Type

Business

Requirements
Must have
• 1. Logo - Nora Quillan Casting
2. Address - 47 Harwick Street
New York, New York 10027
3. Phone - 212-638-4170
4. E-Mail - Casting@noraquillan.com

Nice to have
• Would like the card in black and white with the only accent
color being red.

```html
<!DOCTYPE html>
<html lang="en">
<head>
<meta charset="utf-8">
<title>Nora Quillan Casting – Business Card</title>
<link rel="stylesheet" href="https://fonts.googleapis.com/css2?family=Didact+Gothic&family=Arimo:wght@400&display=swap">
<style>
  :root {
    --page-bg: #e6e4e1;
    --card-top: #1c1c1c;
    --card-bottom: #050505;
    --ink-white: #f2f2f2;
    --accent-red: #e3353d;
  }
  * { box-sizing: border-box; margin: 0; padding: 0; }
  html, body {
    width: 1200px;
    height: 871px;
    overflow: hidden;
    background: var(--page-bg);
  }
  .canvas {
    position: relative;
    width: 1200px;
    height: 871px;
    display: flex;
    align-items: center;
    justify-content: center;
  }
  .card {
    position: relative;
    width: 440px;
    height: 770px;
    background: linear-gradient(180deg, var(--card-top) 0%, var(--card-bottom) 70%);
    box-shadow: 0 18px 40px rgba(0,0,0,0.25);
    overflow: hidden;
  }
  .brand {
    position: absolute;
    top: 78px;
    left: 48px;
    display: flex;
    align-items: center;
    gap: 22px;
  }
  .brand-square {
    width: 64px;
    height: 64px;
    background: var(--accent-red);
    flex: none;
  }
  .brand-name {
    font-family: "Didact Gothic", sans-serif;
    font-size: 42px;
    line-height: 1.05;
    color: var(--ink-white);
  }
  .divider {
    position: absolute;
    left: 0;
    right: 0;
    top: 440px;
    height: 4px;
  }
  .contact {
    position: absolute;
    left: 52px;
    top: 500px;
    list-style: none;
    font-family: "Arimo", sans-serif;
    font-size: 25px;
    line-height: 1.32;
    color: var(--ink-white);
  }
  .contact li {
    display: flex;
    align-items: center;
    gap: 18px;
  }
  .contact-icon {
    width: 16px;
    height: 16px;
    flex: none;
  }
  .contact-icon.blank { visibility: hidden; }
</style>
</head>
<body>
<main class="canvas">
  <article class="card">
    <div class="brand">
      <span class="brand-square"></span>
      <span class="brand-name">Nora<br>Quillan<br>Casting</span>
    </div>

    <svg class="divider" viewBox="0 0 440 4" preserveAspectRatio="none" aria-hidden="true">
      <line x1="4" y1="2" x2="440" y2="2" stroke="var(--accent-red)" stroke-width="3" stroke-linecap="round" stroke-dasharray="0 12"/>
    </svg>

    <ul class="contact">
      <li>
        <svg class="contact-icon" viewBox="0 0 16 16" aria-hidden="true">
          <path d="M4 1.5 L6.5 4.5 L5 6.2 C5.8 8 7.9 10.2 9.8 11 L11.5 9.5 L14.5 12 L12.8 14.3 C7.5 13.8 2.2 8.5 1.7 3.2 Z" fill="var(--accent-red)"/>
        </svg>
        <span>212-638-4170</span>
      </li>
      <li>
        <svg class="contact-icon" viewBox="0 0 16 16" aria-hidden="true">
          <rect x="1" y="3" width="14" height="10" fill="var(--accent-red)"/>
          <path d="M1.5 3.5 L8 9 L14.5 3.5" fill="none" stroke="#111" stroke-width="1.3"/>
        </svg>
        <span>casting@noraquillan.com</span>
      </li>
      <li>
        <svg class="contact-icon" viewBox="0 0 16 16" aria-hidden="true">
          <path d="M8 1 C5 1 3 3.2 3 6 C3 9.5 8 15 8 15 C8 15 13 9.5 13 6 C13 3.2 11 1 8 1 Z" fill="var(--accent-red)"/>
          <circle cx="8" cy="6" r="2" fill="#111"/>
        </svg>
        <span>47 Harwick Street</span>
      </li>
      <li>
        <svg class="contact-icon blank" viewBox="0 0 16 16" aria-hidden="true"></svg>
        <span>New York, New York 10027</span>
      </li>
    </ul>
  </article>
</main>
</body>
</html>
```